Wattle Glen Manor Brochure Design

We need a brochure designed for our Aged Care Facility. We need designs that portray warmth and welcoming and at the same time something professional. We have attached the previous brochure and are looking for a modern professional brochure. We are not set on sizing and welcome ideas.

Attachments:
- One more high res photo is available via this link: https://www.filevaultex.net/s/kq52wpx9trmbe3n/Manor_High-Res_18.jpg?dl=0
- Another high res file has been added and is available through this link:
https://www.filevaultex.net/s/mv71cnd8yhsue6r/Manor_High-Res_24.jpg?dl=0

Target Market(s)

Aged Care and families

Requirements
Must have
• Logo and contact details

```html
<!DOCTYPE html>
<html lang="en">
<head>
<meta charset="utf-8">
<title>Wattle Glen Manor Brochure</title>
<link rel="stylesheet" href="https://fonts.googleapis.com/css2?family=Lato:ital,wght@0,400;0,700;1,400;1,700&display=swap">
<style>
  :root {
    --navy: #1d4566;
    --navy-deep: #163a57;
    --steel: #2f5f80;
    --mist: #d3e0e9;
    --mist-pale: #e8eff4;
    --paper: #f6f8fa;
    --ink: #2b4a63;
    --white: #ffffff;
    --backdrop: #e4e6e8;
  }
  * { box-sizing: border-box; margin: 0; padding: 0; }
  html, body { width: 1200px; height: 804px; overflow: hidden; }
  body {
    background: var(--backdrop);
    font-family: "Lato", Arial, sans-serif;
    color: var(--ink);
    position: relative;
  }
  .page-art { position: absolute; inset: 0; width: 100%; height: 100%; }

  /* Cover */
  .cover {
    position: absolute; left: 30px; top: 140px;
    width: 370px; height: 524px;
    box-shadow: 0 6px 18px rgba(0,0,0,.18);
    overflow: hidden;
  }
  .cover-logo {
    position: absolute; left: 22px; top: 290px;
    width: 180px; height: 100px;
    background: var(--white);
    border-radius: 14px 14px 6px 6px;
    display: flex; flex-direction: column; align-items: center; justify-content: center; gap: 10px;
    padding: 0 10px;
  }
  .cover-logo .mark { width: 30px; height: 30px; border-radius: 50%; background: var(--navy); }
  .cover-logo .name {
    font-size: 12px; font-weight: 700; color: var(--navy);
    letter-spacing: .06em; text-transform: uppercase;
    white-space: nowrap; text-align: center;
  }
  .cover-tagline {
    position: absolute; left: 40px; right: 40px; top: 440px;
    color: var(--white); font-style: italic; font-size: 15px; line-height: 1.35; text-align: center;
  }

  /* Inside spread */
  .spread {
    position: absolute; left: 430px; top: 140px;
    width: 740px; height: 524px;
    box-shadow: 0 6px 18px rgba(0,0,0,.18);
    overflow: hidden;
  }
  .intro {
    position: absolute; left: 30px; top: 150px; width: 315px;
    font-size: 15px; line-height: 1.5; color: var(--steel);
  }
  .testimonial {
    position: absolute; left: 40px; top: 318px; width: 262px;
    background: var(--navy);
    border-radius: 12px 12px 34px 12px;
    padding: 10px 22px 16px 20px;
    color: var(--white); font-size: 11.5px; line-height: 1.45;
  }
  .testimonial .quote-mark {
    display: block; font-size: 40px; font-weight: 700; line-height: .8; height: 24px;
  }
  .testimonial .author {
    display: block; text-align: right; font-weight: 700; font-style: normal;
    margin-top: 8px; font-size: 12px;
  }
  .needs { position: absolute; left: 478px; top: 28px; width: 250px; }
  .provides { position: absolute; left: 400px; top: 206px; width: 228px; }
  .list-heading {
    font-size: 11.5px; font-weight: 700; font-style: italic; color: var(--navy);
    margin-bottom: 5px;
  }
  .feature-list { list-style: none; font-size: 9.5px; line-height: 1.45; color: var(--ink); }
  .feature-list li { padding-left: 9px; position: relative; }
  .feature-list li::before {
    content: ""; position: absolute; left: 0; top: 5px;
    width: 4px; height: 4px; border-radius: 50%; background: var(--navy);
  }
</style>
</head>
<body>

<section class="cover">
  <svg class="page-art" viewBox="0 0 370 524">
    <defs>
      <linearGradient id="coverBg" x1="0" y1="0" x2="0" y2="1">
        <stop offset="0" stop-color="#173c5a"/>
        <stop offset="1" stop-color="#2a5a7c"/>
      </linearGradient>
      <linearGradient id="courtyard" x1="0" y1="0" x2="0" y2="1">
        <stop offset="0" stop-color="#7fb4e0"/>
        <stop offset=".45" stop-color="#c8ccca"/>
        <stop offset="1" stop-color="#8e9c82"/>
      </linearGradient>
    </defs>
    <rect width="370" height="524" fill="url(#coverBg)"/>
    <path d="M0 60 C120 10 260 0 370 20 V0 H0Z" fill="#2b5c80"/>
    <path d="M0 112 C110 70 250 52 370 62 V40 C250 28 110 44 0 92Z" fill="var(--mist)"/>
    <path d="M0 118 C110 78 250 62 370 72 V380 C250 350 110 330 0 336Z" fill="url(#courtyard)" role="img" aria-label="Photo: courtyard of the manor with two residents smiling together on a garden seat"/>
    <path d="M0 336 C110 330 250 350 370 380 V392 C250 362 110 344 0 350Z" fill="var(--mist)"/>
  </svg>
  <div class="cover-logo">
    <span class="mark"></span>
    <span class="name">Wattle Glen Manor</span>
  </div>
  <p class="cover-tagline">Providing aged care with quality, dignity and individuality</p>
</section>

<section class="spread">
  <svg class="page-art" viewBox="0 0 740 524">
    <defs>
      <linearGradient id="paperLeft" x1="0" y1="0" x2="1" y2="1">
        <stop offset="0" stop-color="#ffffff"/>
        <stop offset="1" stop-color="#e9eef2"/>
      </linearGradient>
      <linearGradient id="paperRight" x1="0" y1="0" x2="1" y2="1">
        <stop offset="0" stop-color="#f4f7f9"/>
        <stop offset="1" stop-color="#e3eaef"/>
      </linearGradient>
      <linearGradient id="gutter" x1="0" y1="0" x2="1" y2="0">
        <stop offset="0" stop-color="#000" stop-opacity="0"/>
        <stop offset=".5" stop-color="#000" stop-opacity=".12"/>
        <stop offset="1" stop-color="#000" stop-opacity="0"/>
      </linearGradient>
    </defs>
    <rect width="370" height="524" fill="url(#paperLeft)"/>
    <rect x="370" width="370" height="524" fill="url(#paperRight)"/>
    <path d="M0 0 H370 V120 C250 130 120 135 0 140Z" fill="var(--paper)"/>
    <path d="M0 410 C120 330 260 300 370 300 V524 H0Z" fill="var(--mist-pale)"/>
    <rect x="0" y="40" width="52" height="84" rx="10" fill="#4d86b3" role="img" aria-label="Photo: coastal view in soft blue tones"/>
    <rect x="68" y="36" width="132" height="88" rx="10" fill="#b8aab4" role="img" aria-label="Photo: bright resident lounge room with sofas"/>
    <rect x="216" y="34" width="130" height="92" rx="10" fill="#b4a47a" role="img" aria-label="Photo: furnished resident bedroom with bedside lamp"/>
    <path d="M630 205 C665 165 710 155 740 157 V265 C710 265 665 258 630 205Z" fill="var(--mist)"/>
    <path d="M652 205 C680 177 715 170 740 172 V252 C715 252 680 246 652 205Z" fill="#c7b7ad" role="img" aria-label="Photo: two residents chatting in a sunny room"/>
    <rect x="355" width="30" height="524" fill="url(#gutter)"/>
  </svg>

  <p class="intro">Wattle Glen Manor is an accredited Government funded place, a facility offering quality, dignity and individuality to residents and their loved ones.</p>

  <blockquote class="testimonial">
    <span class="quote-mark">&ldquo;</span>
    <p>Overall our mother is happier, she initiates conversation, her memory has improved. She laughs a lot &amp; still beats some of us at maths. Her &ldquo;spark&rdquo; seems to have returned. That makes the whole family happy.</p>
    <cite class="author">Maree Holden</cite>
  </blockquote>

  <div class="needs">
    <h3 class="list-heading">If you need...</h3>
    <ul class="feature-list">
      <li>Low level or high level respite care</li>
      <li>Permanent Care</li>
      <li>Differing levels of care for you and your spouse together</li>
      <li>Specific dementia care and expertise</li>
      <li>Experienced and caring staff</li>
      <li>High quality accommodation and facilities</li>
      <li>A home where your family are welcomed</li>
      <li>Day Care Dementia</li>
    </ul>
  </div>

  <div class="provides">
    <h3 class="list-heading">Wattle Glen Manor provides...</h3>
    <ul class="feature-list">
      <li>Large spacious rooms with ensuites</li>
      <li>A specialised dementia section</li>
      <li>Extensive kitchen, laundry and staff facilities</li>
      <li>Care for couples with differing levels of care so they can remain together</li>
      <li>Qualified and experienced nursing staff</li>
      <li>Diversional Therapists</li>
      <li>Home theatre room</li>
      <li>Hairdressing salon on site</li>
      <li>Doctor and therapist consulting rooms</li>
      <li>Spacious dining room</li>
      <li>Open lounges with library, internet, fireplace and recreation</li>
      <li>Tranquil leafy outdoor areas and indoor garden courtyard including BBQ and picnic grounds</li>
      <li>Common areas to enjoy and entertain visitors</li>
      <li>Specialised dementia wellness program as designed by Graham Pettit (Don)</li>
    </ul>
  </div>
</section>

</body>
</html>
```